High End Notary Service Business Card Design

Want a professional and elegant/luxurious business card that is clean and simple in the design. A notary is a trusted professional that helps people sign very important documents. The card should be in alignment with this service provided.

Most of the time, service will be for the purchase of a home or refinance of a mortgage

There is NO LOGO. This is aesthetic. A look and feel. Conveying professionalism and concierge level of service.

Target Market(s)

Other business professionals, Lawyers, Escrow Officers, Loan Officers

Industry/Entity Type

Legal

Contact Information for Business Card

This will be a one-sided business card

Colors
35a7d7
3176b5
85cae6
d3a5cc
b868aa
ffffff
0356a4

Requirements
Must have
• Doreen L. Marsh-Whitlock
Notary Public

614-872-3916
MarshPublicNotary@Vornmail.com
Nice to have
• Headshot photo below. Convey the aspect of signing documents. No black cards. Preference is shades of blue: light blue, navy, aqua, gold, white, or lavendar, etc.
Should not have
• No scales or legal scales.

```html
<!DOCTYPE html>
<html lang="en">
<head>
<meta charset="utf-8">
<title>Doreen L. Marsh-Whitlock — Notary Public</title>
<link rel="stylesheet" href="https://fonts.googleapis.com/css2?family=Bebas+Neue&display=swap">
<style>
  :root {
    --stage: #9c9c9c;
    --card: #ffffff;
    --name-blue: #3176b5;
    --icon-navy: #0356a4;
    --text-grey: #6b6b6b;
    --rule-grey: #c9c9c9;
    --photo-top: #8d91a6;
    --photo-mid: #9a98a8;
    --photo-low: #d7b6a0;
  }
  * { margin: 0; padding: 0; box-sizing: border-box; }
  html, body {
    width: 1200px;
    height: 1200px;
    overflow: hidden;
    background: var(--stage);
  }
  .business-card {
    position: absolute;
    left: 278px;
    top: 74px;
    width: 645px;
    height: 1052px;
    background: var(--card);
    box-shadow: 3px 4px 8px rgba(0,0,0,0.35);
    font-family: "Bebas Neue", "Oswald", sans-serif;
    text-align: center;
  }
  .headshot {
    position: absolute;
    left: 121px;
    top: 63px;
    width: 403px;
    height: 440px;
    border-radius: 50%;
    background:
      radial-gradient(ellipse 45% 55% at 50% 45%, var(--photo-low) 0%, var(--photo-mid) 60%, transparent 75%),
      linear-gradient(180deg, var(--photo-top) 0%, var(--photo-mid) 100%);
  }
  .line {
    position: absolute;
    left: 0;
    width: 100%;
    line-height: 1;
    white-space: nowrap;
  }
  .holder-name {
    top: 538px;
    font-size: 63px;
    color: var(--name-blue);
  }
  .holder-title {
    top: 601px;
    font-size: 63px;
    color: var(--text-grey);
  }
  .phone-number {
    top: 752px;
    font-size: 77px;
    color: var(--text-grey);
  }
  .email-address {
    top: 930px;
    font-size: 49px;
    color: var(--text-grey);
  }
  .divider {
    position: absolute;
    left: 178px;
    width: 290px;
    height: 60px;
  }
  .divider-phone { top: 678px; }
  .divider-email { top: 856px; }
</style>
</head>
<body>
  <div class="business-card">
    <div class="headshot" role="img" aria-label="Headshot portrait of the notary"></div>

    <div class="line holder-name">Doreen L. Marsh-Whitlock</div>
    <div class="line holder-title">Notary Public</div>

    <svg class="divider divider-phone" viewBox="0 0 290 60" aria-hidden="true">
      <line x1="0" y1="30" x2="104" y2="30" stroke="var(--rule-grey)" stroke-width="1.5"/>
      <line x1="181" y1="30" x2="290" y2="30" stroke="var(--rule-grey)" stroke-width="1.5"/>
      <circle cx="143" cy="30" r="30" fill="var(--icon-navy)"/>
      <path d="M136 17 c-3 1 -5 4 -5 8 c0 8 7 18 14 20 c3 1 6 0 8 -2 l-4 -6 c-1 -1 -2 -1 -3 0 l-2 1 c-3 -2 -6 -7 -6 -11 l2 -1 c1 -1 1 -2 1 -3 z" fill="#ffffff"/>
    </svg>

    <div class="line phone-number">614-872-3916</div>

    <svg class="divider divider-email" viewBox="0 0 290 60" aria-hidden="true">
      <line x1="0" y1="30" x2="104" y2="30" stroke="var(--rule-grey)" stroke-width="1.5"/>
      <line x1="181" y1="30" x2="290" y2="30" stroke="var(--rule-grey)" stroke-width="1.5"/>
      <circle cx="143" cy="30" r="30" fill="var(--icon-navy)"/>
      <rect x="125" y="20" width="36" height="22" fill="none" stroke="#ffffff" stroke-width="2"/>
      <polyline points="125,20 143,33 161,20" fill="none" stroke="#ffffff" stroke-width="2"/>
      <line x1="125" y1="42" x2="138" y2="30" stroke="#ffffff" stroke-width="1.5"/>
      <line x1="161" y1="42" x2="148" y2="30" stroke="#ffffff" stroke-width="1.5"/>
    </svg>

    <div class="line email-address">MarshPublicNotary@Vornmail.com</div>
  </div>
</body>
</html>
```